Flyer für Zeitarbeitsfirma
Zielgruppe
Wir sind eine Zeitarbeitsfirma in der Pflege! Unsere Kunden sind Krankenhäuser und Pflegeheime
Aufgabenstellung
Wir möchten eine Art Flyer als erste Seite einer Bewerbungsmappe.
Überschrift: Bewerbung als Personaldienstleister
Warum K7-CURAVIT?
Wir bieten entscheidende Unterschiede:
1 Tag KOSTENFREI
(Vermindern Sie Ihr Risiko für schlechtes Zeitarbeitspersonal)
5 Tage günstiger Einarbeitungstarif
anschließend erhalten Sie eine Preisgarantie fürs gesamte Jahr
PLUS kostenfreie Übernahme unserer Mitarbeiter
Worauf warten Sie noch?
Wir freuen uns auf eine tolle Zusammenarbeit!
www.kobalt-7.de

```html
<!DOCTYPE html>
<html lang="de">
<head>
<meta charset="utf-8">
<title>Bewerbung als Personaldienstleister – K7-CURAVIT</title>
<link rel="stylesheet" href="https://fonts.googleapis.com/css2?family=Inter:wght@400;600;700;800&display=swap">
<style>
  :root {
    --green-deep: #0b9a40;
    --green-soft: #4fb87a;
    --green-text: #0a9a3f;
    --grey-text: #5a5a5a;
    --white: #ffffff;
    --photo-light: #d8dadb;
    --photo-mid: #c2c8cc;
    --photo-warm: #ddd8d1;
  }
  * { margin: 0; padding: 0; box-sizing: border-box; }
  html, body { width: 848px; height: 1200px; overflow: hidden; background: var(--white); }
  body { font-family: "Inter", Arial, sans-serif; position: relative; }

  .hero-photo {
    position: absolute; left: 0; top: 0; width: 848px; height: 606px;
    background: linear-gradient(100deg, var(--photo-light) 0%, var(--photo-mid) 50%, var(--photo-warm) 100%);
  }

  .title-band {
    position: absolute; left: 0; top: 423px; width: 665px; height: 183px;
    background: var(--green-deep); opacity: 0.82;
  }
  .title {
    position: absolute; left: 37px; top: 462px; color: var(--white);
    letter-spacing: -0.055em;
  }
  .title-lead { font-size: 38px; font-weight: 400; line-height: 1; }
  .title-main { font-size: 58px; font-weight: 800; line-height: 1.05; margin-top: 2px; }

  .offer-box {
    position: absolute; left: 0; top: 606px; width: 665px; height: 254px;
    background: var(--green-soft); color: var(--white);
  }
  .offer { position: absolute; letter-spacing: -0.05em; }
  .offer-head { font-size: 31px; font-weight: 700; line-height: 1; }
  .offer-note { font-size: 17.5px; font-weight: 400; line-height: 1; margin-top: 19px; letter-spacing: -0.045em; }
  .offer-free { left: 42px; top: 40px; }
  .offer-free .offer-note { margin-left: -1px; }
  .offer-rate { left: 37px; top: 144px; }

  .plus-line {
    position: absolute; left: 37px; top: 894px;
    font-size: 28.5px; font-weight: 700; color: var(--green-text);
    letter-spacing: -0.055em;
  }

  .closing {
    position: absolute; left: 42px; top: 1012px;
    font-size: 31.5px; font-weight: 400; color: var(--grey-text);
    line-height: 45px; letter-spacing: -0.055em;
  }

  .brand {
    position: absolute; left: 600px; top: 1032px; width: 220px;
    display: flex; flex-direction: column; align-items: center; gap: 10px;
  }
  .brand-dot {
    width: 90px; height: 90px; border-radius: 50%; background: var(--green-deep);
  }
  .brand-name {
    font-size: 22px; font-weight: 700; color: var(--green-deep); letter-spacing: -0.03em;
  }
</style>
</head>
<body>
  <div class="hero-photo" role="img" aria-label="Foto: Pflegekraft in blauer Dienstkleidung, im Hintergrund ein Ärzteteam im Klinikflur"></div>
  <div class="title-band"></div>
  <h1 class="title">
    <div class="title-lead">Bewerbung als</div>
    <div class="title-main">Personaldienstleister</div>
  </h1>

  <section class="offer-box">
    <div class="offer offer-free">
      <div class="offer-head">1 Tag KOSTENFREI</div>
      <div class="offer-note">(Vermindern Sie Ihr Risiko für schlechtes Zeitarbeitspersonal)</div>
    </div>
    <div class="offer offer-rate">
      <div class="offer-head">5 Tage günstiger Einarbeitungstarif</div>
      <div class="offer-note">anschließend erhalten Sie eine Preisgarantie fürs gesamte Jahr</div>
    </div>
  </section>

  <p class="plus-line">+ kostenfreie Übernahme unserer Mitarbeiter</p>

  <p class="closing">Worauf warten Sie noch?<br>Wir freuen uns auf eine tolle<br>Zusammenarbeit!</p>

  <div class="brand">
    <span class="brand-dot"></span>
    <span class="brand-name">K7-CURAVIT</span>
  </div>
</body>
</html>
```